Steadfast Voyage Partners Capability Statement

Steadfast Voyage Partners is a Corporate Travel Management company based in Brisbane, Australia. Please review our 'About Us' page of our website to gain an understanding of our company culture (www.steadfastvoyagepartners.example.com.au). We are extremely customer focused. We see ourselves as an extension of our client's business.We require a powerful 1 page infographic that highlights what we do - 'Capability Statement' to use as an initial introduction to prospect clients when they ask for information about us.* Our Core Competencies - Service / People / Technology (this is our tagline so I think the document should follow this format)* A Company snapshot - Office location and website (needs to be editable to add Licence information)* Performance / Key Benefits (needs to editable to add in testimonials and case studies)* Client retention result 96%* Employee retention 98%* Affiliations & Partnerships (we will add)*Awards (see details to include)* Contact Details (at the bottom of the page - Marcus Van Heerden marcus@svpartners.example.com.au+61 448 187 226Differentiators (for us to complete so doc must be editable)The format of the document needs to be easily modified when required. I have attached the company logos and branding colours / font etc. Thank youRegardsMiriam

Target Market(s)

Medium businesses Australian based

Industry/Entity Type

Travel Industry

Font styles to use
Sans Serif

Colors
abd036

Requirements
Must have
• Content Outlined and corporate colours. Must be easily editable.

```html
<!DOCTYPE html>
<html lang="en">
<head>
<meta charset="utf-8">
<title>Steadfast Voyage Partners – Capability Statement</title>
<link href="https://fonts.googleapis.com/css2?family=Bebas+Neue&family=Montserrat:wght@600;700&family=Nunito+Sans:wght@400;700&display=swap" rel="stylesheet">
<style>
  :root{
    --backdrop:#e9e4e2;
    --paper:#f2f2f2;
    --green:#57b947;
    --green-light:#abd036;
    --green-soft:#9fd86a;
    --ink:#2b2b2b;
    --ink-soft:#444;
    --footer-dark:#333;
    --hex-fill:#e4e4e4;
  }
  *{margin:0;padding:0;box-sizing:border-box}
  html,body{width:1200px;height:890px;overflow:hidden;background:var(--backdrop)}
  .stage{position:relative;width:1200px;height:890px}
  .sheet{
    position:absolute;left:296px;top:14px;width:558px;height:790px;
    transform:scale(1.09);transform-origin:top left;
    background:var(--paper);overflow:hidden;
    font-family:"Nunito Sans",Arial,sans-serif;color:var(--ink);
    box-shadow:0 2px 10px rgba(0,0,0,.12);
  }
  .hero{position:absolute;left:0;top:0;width:558px;height:340px}
  .brand{position:absolute;left:22px;top:32px;display:flex;align-items:center;gap:8px}
  .brand-mark{width:16px;height:16px;background:var(--green)}
  .brand-name{font-weight:700;font-size:17px;line-height:1;color:var(--ink-soft);width:190px}
  .about{position:absolute;left:0;top:350px;width:558px;text-align:center}
  .about-title{font-family:"Bebas Neue",sans-serif;font-size:41px;line-height:40px;font-weight:400;letter-spacing:.5px}
  .about-rule{width:92px;height:1.5px;background:var(--ink);margin:0 auto 10px}
  .about-lead{width:480px;margin:0 auto 6px;font-weight:700;font-size:10.2px;line-height:13.5px}
  .about-body{width:480px;margin:0 auto;font-size:10.2px;line-height:13.5px;color:var(--ink-soft)}
  .diagram{position:absolute;left:0;top:485px;width:558px;height:265px}
  .pill{
    position:absolute;display:flex;align-items:center;justify-content:center;text-align:center;
    width:124px;height:40px;border:1.3px solid var(--green-soft);border-radius:7px;background:#f6f6f6;
    font-family:"Montserrat",sans-serif;font-weight:700;font-size:7.6px;line-height:10.5px;color:var(--ink);
  }
  .pill-snapshot{left:208px;top:5px}
  .pill-core{left:62px;top:78px}
  .pill-performance{left:350px;top:78px}
  .pill-affiliations{left:62px;top:145px}
  .pill-client{left:350px;top:145px}
  .pill-employee{left:209px;top:218px}
  .hub-name{position:absolute;left:226px;top:124px;width:80px;text-align:center;font-weight:700;font-size:7px;line-height:8px;color:var(--ink-soft)}
  .footer{position:absolute;left:0;bottom:0;width:558px;height:42px}
  .footer-text{position:absolute;left:0;bottom:9px;width:558px;text-align:center;color:#fff;font-family:"Montserrat",sans-serif;font-weight:600;font-size:8.6px;line-height:12px}
  .footer-text svg{vertical-align:-1px;margin-right:2px}
</style>
</head>
<body>
<div class="stage">
  <article class="sheet">
    <svg class="hero" viewBox="0 0 558 340" aria-hidden="false">
      <defs>
        <linearGradient id="photoTone" x1="0" y1="0" x2="0" y2="1">
          <stop offset="0" stop-color="#c9d3df"/>
          <stop offset=".5" stop-color="#dcd8d2"/>
          <stop offset=".72" stop-color="#a89276"/>
          <stop offset="1" stop-color="#5e4c3c"/>
        </linearGradient>
        <linearGradient id="swoosh" x1="0" y1="0" x2="1" y2="0">
          <stop offset="0" stop-color="#8cc63f"/>
          <stop offset="1" stop-color="#3fae49"/>
        </linearGradient>
      </defs>
      <path role="img" aria-label="Photo: airliner parked outside an airport lounge window with rows of seats"
            d="M0 140 C150 105 330 60 558 52 L558 328 L0 328 Z" fill="url(#photoTone)"/>
      <path d="M0 128 C170 95 330 55 558 30 L558 52 C330 60 150 105 0 140 Z" fill="url(#swoosh)"/>
      <path d="M0 118 C200 110 320 20 418 0 L380 0 C300 20 190 98 0 112 Z" fill="var(--green-light)"/>
      <rect x="0" y="328" width="558" height="7" fill="var(--green)"/>
    </svg>
    <div class="brand">
      <span class="brand-mark"></span>
      <span class="brand-name">Steadfast Voyage Partners</span>
    </div>

    <section class="about">
      <h1 class="about-title">About Us</h1>
      <div class="about-rule"></div>
      <p class="about-lead">Steadfast Voyage Partners was founded on the vision of delivering a superior customer experience and end to end business travel management solutions.</p>
      <p class="about-body">Opening for business in 2005, SVP is a progressive business travel management company and corporate travel specialist. We focus on engaging industry-best consultants and market leading technology, including Routewise Atlas, to provide a tailored, complete, personalised business travel offering.</p>
    </section>

    <section class="diagram">
      <svg width="558" height="265" viewBox="0 0 558 265">
        <polygon points="264,61 324,96 327,160 266,198 206,161 207,94" fill="none" stroke="var(--green)" stroke-width="3"/>
        <polygon points="265,88 305,111 305,153 265,176 225,153 225,111" fill="var(--hex-fill)" stroke="#d0d0d0"/>
        <g fill="var(--green)" stroke="#fff" stroke-width="2.5">
          <circle cx="264" cy="61" r="12"/><circle cx="324" cy="96" r="12"/><circle cx="327" cy="160" r="12"/>
          <circle cx="266" cy="198" r="12"/><circle cx="206" cy="161" r="12"/><circle cx="207" cy="94" r="12"/>
        </g>
        <g fill="#fff" font-family="Montserrat,sans-serif" font-weight="700" font-size="11" text-anchor="middle">
          <text x="207" y="98">1</text><text x="264" y="65">2</text><text x="324" y="100">3</text>
          <text x="327" y="164">4</text><text x="266" y="202">5</text><text x="206" y="165">6</text>
        </g>
      </svg>
      <div class="pill pill-snapshot">A COMPANY SNAPSHOT</div>
      <div class="pill pill-core">OUR CORE COMPETENCIES</div>
      <div class="pill pill-performance">PERFORMANCE / KEY<br>BENEFITS</div>
      <div class="pill pill-affiliations">AFFILIATIONS &amp;<br>PARTNERSHIPS</div>
      <div class="pill pill-client">CLIENT RETENTION RESULT<br>96%</div>
      <div class="pill pill-employee">EMPLOYEE RETENTION<br>98%</div>
      <div class="hub-name">Steadfast Voyage Partners</div>
    </section>

    <footer class="footer">
      <svg width="558" height="42" viewBox="0 0 558 42">
        <rect x="0" y="27" width="558" height="15" fill="var(--footer-dark)"/>
        <polygon points="100,0 430,0 486,42 44,42" fill="var(--footer-dark)"/>
        <polygon points="103,3 427,3 450,42 82,42" fill="var(--green)"/>
      </svg>
      <div class="footer-text">
        <div><svg width="7" height="9" viewBox="0 0 7 9"><path d="M3.5 0A3.2 3.2 0 0 0 .3 3.2C.3 5.6 3.5 9 3.5 9s3.2-3.4 3.2-5.8A3.2 3.2 0 0 0 3.5 0Zm0 4.4a1.2 1.2 0 1 1 0-2.4 1.2 1.2 0 0 1 0 2.4Z" fill="#fff"/></svg>Marcus Van Heerden marcus@svpartners.example.com.au</div>
        <div><svg width="8" height="8" viewBox="0 0 8 8"><path d="M1.6.3 2.8 2 2 3a4.6 4.6 0 0 0 3 3l1-.8 1.7 1.2-.6 1.2C3.6 7.7.3 4.4.4.9Z" fill="#fff"/></svg>+61 455 903 618</div>
      </div>
    </footer>
  </article>
</div>
</body>
</html>
```